TBrenwick Business Cards & Letterhead

I have a logo but need a design for some new business cards. We are a Design-Build Firm that specializes in the design and construction of commercial projects.
the cards need to be professional. no cartoon stuff.
i would like to have the cards in AI format so I can update the card as needed. Logo is provided.
Our Address is: 4718 Fenmoor Ct. Dunmere, West Calloway 60418

```html
<!DOCTYPE html>
<html lang="en">
<head>
<meta charset="utf-8">
<title>TBrenwick Business Card</title>
<link href="https://fonts.googleapis.com/css2?family=Roboto:wght@400;500;700;900&display=swap" rel="stylesheet">
<style>
  :root {
    --page-bg: #3b3b3b;
    --card-white: #f6f6f6;
    --brand-blue: #0a6aa6;
    --brand-blue-deep: #005a8e;
    --brand-blue-light: #0a77b6;
    --text-grey: #444444;
    --muted-grey: #6a6a6a;
    --logo-grey: #4d4d4d;
    --rule: #333333;
  }
  html, body {
    margin: 0;
    width: 1200px;
    height: 1200px;
    overflow: hidden;
    background: var(--page-bg);
    font-family: "Roboto", Arial, sans-serif;
  }
  .canvas {
    position: relative;
    width: 1200px;
    height: 1200px;
  }
  .card {
    position: absolute;
    left: 200px;
    width: 800px;
    height: 457px;
    border-radius: 26px;
    overflow: hidden;
  }
  .card-front {
    top: 120px;
    background: var(--card-white);
  }
  .card-front .bottom-band {
    position: absolute;
    left: 0; right: 0; bottom: 0;
    height: 19px;
    background: linear-gradient(90deg, var(--brand-blue-deep), var(--brand-blue-light), var(--brand-blue-deep));
  }
  .wordmark {
    position: absolute;
    right: 52px;
    top: 62px;
    font-weight: 900;
    font-size: 50px;
    letter-spacing: 0.5px;
    color: var(--logo-grey);
    line-height: 1;
    display: flex;
    align-items: center;
    gap: 12px;
  }
  .wordmark .mark-square {
    width: 34px;
    height: 34px;
    background: var(--brand-blue);
  }
  .person {
    position: absolute;
    left: 55px;
    top: 256px;
  }
  .person-name {
    margin: 0;
    font-size: 29px;
    font-weight: 700;
    color: var(--brand-blue);
    line-height: 1.1;
  }
  .person-title {
    margin: 2px 0 0;
    font-size: 17px;
    color: var(--muted-grey);
  }
  .divider {
    position: absolute;
    left: 55px;
    right: 55px;
    top: 321px;
    height: 1px;
    background: var(--rule);
  }
  .contacts {
    position: absolute;
    left: 54px;
    top: 333px;
    margin: 0;
    padding: 0;
    list-style: none;
    font-size: 19px;
    color: var(--text-grey);
    line-height: 23.5px;
  }
  .contacts li {
    display: flex;
    align-items: center;
    gap: 10px;
  }
  .contacts svg { width: 16px; height: 16px; flex: none; }
  .address {
    position: absolute;
    right: 55px;
    top: 336px;
    margin: 0;
    text-align: right;
    font-style: normal;
    font-size: 19px;
    color: var(--text-grey);
    line-height: 24px;
  }
  .address .web { color: var(--brand-blue); margin-right: -4px; }
  .card-back {
    top: 660px;
    background: radial-gradient(ellipse at 50% 40%, #0a72ae 0%, #06659f 45%, #005486 100%);
    display: flex;
    align-items: center;
    justify-content: center;
  }
  .back-wordmark {
    font-weight: 900;
    font-size: 64px;
    letter-spacing: 1px;
    color: #1a86c4;
    display: flex;
    align-items: center;
    gap: 18px;
  }
  .back-wordmark .mark-square {
    width: 46px;
    height: 46px;
    background: #1a86c4;
  }
</style>
</head>
<body>
<main class="canvas">
  <section class="card card-front" aria-label="Business card front">
    <div class="wordmark"><span class="mark-square"></span>TBRENWICK</div>

    <div class="person">
      <h1 class="person-name">Martin Hale</h1>
      <p class="person-title">Managing Director</p>
    </div>

    <div class="divider"></div>

    <ul class="contacts">
      <li>
        <svg viewBox="0 0 16 16" aria-hidden="true"><path fill="#0a6aa6" d="M3.6 1.2l2.2 2.6c.3.4.3.9 0 1.3L4.8 6.3c.8 1.8 2.4 3.4 4.2 4.3l1.2-1c.4-.3.9-.3 1.3 0l2.6 2.2c.4.3.4.9.1 1.3l-1.4 1.5c-.5.5-1.2.6-1.8.4C6.4 13.4 2.7 9.6 1 5c-.2-.6-.1-1.3.4-1.8l1.5-1.4c.4-.4.9-.3 1.2 0z"/></svg>
        <span>555-210-4872</span>
      </li>
      <li>
        <svg viewBox="0 0 16 16" aria-hidden="true"><rect x="3.5" y="0.8" width="9" height="14.4" rx="1.5" fill="none" stroke="#0a6aa6" stroke-width="1.8"/><rect x="6.5" y="12.2" width="3" height="1.3" fill="#0a6aa6"/></svg>
        <span>555-318-6091</span>
      </li>
      <li>
        <svg viewBox="0 0 16 16" aria-hidden="true"><rect x="1" y="3.5" width="14" height="9.5" fill="#0a6aa6"/><path d="M1.5 4l6.5 5 6.5-5" fill="none" stroke="#f6f6f6" stroke-width="1.2"/></svg>
        <span>info@tbrenwick.com</span>
      </li>
    </ul>

    <address class="address">
      4718 Fenmoor Ct. Dunmere<br>
      West Calloway 60418<br>
      <span class="web">www.tbrenwick.com</span>
    </address>

    <div class="bottom-band"></div>
  </section>

  <section class="card card-back" aria-label="Business card back">
    <div class="back-wordmark"><span class="mark-square"></span>TBRENWICK</div>
  </section>
</main>
</body>
</html>
```